Business Card For Life Coaching Business For Men

Take my existing logo and apply it to a business card. I would like the logo to be prominent with stylistic text below reading Life Coaching For Men. Contact info should show as:
Dale Hartwig
dale@steadforgepath.com

```html
<!DOCTYPE html>
<html lang="en">
<head>
<meta charset="UTF-8">
<title>Steadforge Path – Business Card</title>
<link href="https://fonts.googleapis.com/css2?family=Montserrat:ital,wght@0,400;0,500;0,600;0,700;0,800&family=Dancing+Script:wght@600&display=swap" rel="stylesheet">
<style>
  :root{
    --backdrop:#1f2023;
    --navy:#2e2a82;
    --teal:#0f8a8a;
    --steel:#7f9cc0;
    --white:#ffffff;
  }
  *{box-sizing:border-box;margin:0;padding:0}
  html,body{width:1200px;height:840px;overflow:hidden}
  body{
    background:var(--backdrop);
    font-family:'Montserrat',sans-serif;
    display:flex;align-items:center;justify-content:center;gap:40px;
  }
  .card{
    width:540px;height:316px;border-radius:24px;position:relative;
    box-shadow:0 5px 0 var(--teal),0 18px 30px rgba(0,0,0,.45);
    overflow:hidden;
  }
  /* back side */
  .card-back{background:var(--navy);color:var(--white);display:flex;flex-direction:column;align-items:center;padding:52px 34px 0}
  .brand{display:flex;align-items:center;gap:16px}
  .brand-dot{width:64px;height:64px;border-radius:50%;flex:none}
  .card-back .brand-dot{border:7px solid var(--white)}
  .brand-name{font-weight:800;text-transform:uppercase;line-height:.98;letter-spacing:.5px}
  .card-back .brand-name{font-size:40px;color:var(--white)}
  .pitch{margin-top:38px;text-align:center;font-size:11.6px;line-height:1.45;font-weight:400}
  .pitch strong{display:block;font-weight:600;font-size:12px;margin-top:2px}

  /* front side */
  .card-front{background:var(--white);display:flex;align-items:center;padding:0 30px 0 34px}
  .card-front .brand{gap:10px;width:210px}
  .card-front .brand-dot{width:40px;height:40px;border:5px solid var(--steel)}
  .card-front .brand-name{font-size:24px;color:var(--navy)}
  .divider{width:2px;height:150px;background:var(--teal);margin:0 24px 40px 6px;flex:none}
  .details{margin-bottom:40px}
  .person{font-weight:800;font-size:22px;letter-spacing:.5px;text-transform:uppercase;color:var(--navy)}
  .person .surname{color:var(--teal)}
  .role{font-size:13px;color:var(--navy);font-weight:500;margin-top:2px}
  .contacts{list-style:none;margin-top:18px}
  .contacts li{display:flex;align-items:center;gap:8px;font-size:12.5px;color:var(--navy);margin-bottom:6px}
  .contacts svg{width:13px;height:13px;flex:none;fill:var(--teal)}
  .tagline{
    position:absolute;left:0;right:0;bottom:30px;text-align:center;padding-left:120px;
    font-family:'Dancing Script',cursive;font-size:22px;color:var(--navy);
  }
</style>
</head>
<body>

  <section class="card card-back">
    <div class="brand">
      <span class="brand-dot"></span>
      <span class="brand-name">Steadforge<br>Path</span>
    </div>
    <p class="pitch">
      One-on-one coaching for men looking for new directions in: Career, Finances, Health,<br>
      Love, Spirituality We offer: --One-on-one Coaching --Group Coaching --Webinars
      <strong>Find The Path That Is Right For You</strong>
    </p>
  </section>

  <section class="card card-front">
    <div class="brand">
      <span class="brand-dot"></span>
      <span class="brand-name">Steadforge<br>Path</span>
    </div>
    <span class="divider"></span>
    <div class="details">
      <h1 class="person">Dale <span class="surname">Hartwig</span></h1>
      <p class="role">Certified Life Coach</p>
      <ul class="contacts">
        <li><svg viewBox="0 0 24 24"><path d="M6.6 10.8a15.1 15.1 0 0 0 6.6 6.6l2.2-2.2a1 1 0 0 1 1-.25 11.4 11.4 0 0 0 3.6.57 1 1 0 0 1 1 1V20a1 1 0 0 1-1 1A17 17 0 0 1 3 4a1 1 0 0 1 1-1h3.5a1 1 0 0 1 1 1c0 1.25.2 2.45.57 3.57a1 1 0 0 1-.25 1z"/></svg>555.014.2290</li>
        <li><svg viewBox="0 0 24 24"><path d="M2 5h20v14H2z M3 6l9 7 9-7" /></svg>dale@steadforgepath.com</li>
        <li><svg viewBox="0 0 24 24"><circle cx="12" cy="12" r="10"/></svg>www.steadforgepath.com</li>
      </ul>
    </div>
    <p class="tagline">Life Coaching For Men</p>
  </section>

</body>
</html>
```